Australian residential property business needs a business card design

I need a business card design for my new business 'Meadow Estate Partners'. The business will involve house purchases, land development sites, renovation projects, sub-divisions etc. I will be buying property from motivated vendors and working with property investors. I will deal with a wide range of people working in the residential property market including real estate agents, councils, tradespeople, banks, home owners, etc.

I would like something simple, not flashy, but a little bit unique. The colours should be in line with my logo. The business card needs to be professional. I would like something memorable, but not 'busy' or too bright. Not boring. Modern ok.

Target Market(s)

Home owners looking to sell their property, real estate agents, tradespeople (e.g. plumbers, builders, electricians etc), property investors, local councils, and anyone else involved in the residential property industry

Industry/Entity Type

Business

Contact Information for Business Card

I need to include my business name/logo, my name, my title, a PO Box number/address, a mobile number, and an email address.

Font styles to use
Serif

Requirements
Must have
• My business card details listed above.

```html
<!DOCTYPE html>
<html lang="en">
<head>
<meta charset="utf-8">
<title>Meadow Estate Partners – Business Card</title>
<link rel="stylesheet" href="https://fonts.googleapis.com/css2?family=Lora:wght@400;600&display=swap">
<style>
  :root {
    --page-bg: #e9e6e0;
    --card-white: #f7f7f5;
    --brand-green: #1aa25f;
    --brand-green-deep: #0f8a4c;
    --brand-gold: #e9a81f;
    --ink-dark: #333333;
    --ink-light: #ffffff;
  }
  html, body {
    margin: 0;
    width: 1200px;
    height: 600px;
    overflow: hidden;
    background: var(--page-bg);
    font-family: "Lora", Georgia, serif;
  }
  .business-card {
    position: absolute;
    left: 250px;
    top: 100px;
    width: 700px;
    height: 400px;
    background: var(--card-white);
    box-shadow: 0 6px 18px rgba(0,0,0,0.18);
    overflow: hidden;
  }
  .card-wave {
    position: absolute;
    inset: 0;
  }
  .brand-name {
    position: absolute;
    left: 300px;
    top: 78px;
    display: flex;
    align-items: center;
    gap: 12px;
    color: var(--brand-gold);
    font-weight: 600;
    font-size: 21px;
    letter-spacing: 1px;
    line-height: 1.2;
    text-transform: uppercase;
  }
  .brand-dot {
    width: 24px;
    height: 24px;
    border-radius: 50%;
    background: var(--brand-gold);
    flex: none;
  }
  .holder {
    position: absolute;
    left: 60px;
    top: 186px;
  }
  .holder-name {
    margin: 0;
    color: var(--brand-green);
    font-size: 22px;
    font-weight: 400;
  }
  .holder-title {
    margin: 2px 0 0;
    color: var(--ink-dark);
    font-size: 12px;
  }
  .contact-list {
    position: absolute;
    left: 130px;
    top: 306px;
    margin: 0;
    padding: 0;
    list-style: none;
    color: var(--ink-light);
    font-size: 12px;
    line-height: 1.55;
  }
  .contact-list li {
    display: flex;
    align-items: center;
    gap: 8px;
  }
  .contact-icon {
    width: 12px;
    height: 12px;
    flex: none;
  }
  .contact-indent { padding-left: 20px; }
</style>
</head>
<body>
  <div class="business-card">
    <svg class="card-wave" viewBox="0 0 700 400" width="700" height="400" aria-hidden="true">
      <path d="M0,262 C200,292 390,262 505,180 C585,122 612,45 636,0 L700,0 L700,400 L0,400 Z" fill="var(--brand-gold)"/>
      <path d="M0,271 C200,301 395,272 513,190 C594,132 622,52 648,0 L700,0 L700,400 L0,400 Z" fill="var(--brand-green)"/>
      <path d="M0,345 C260,360 470,310 600,210 C650,170 680,125 700,90 L700,400 L0,400 Z" fill="var(--brand-green-deep)" opacity="0.25"/>
    </svg>

    <div class="brand-name">
      <span class="brand-dot"></span>
      <span>Meadow Estate<br>Partners</span>
    </div>

    <div class="holder">
      <p class="holder-name">Daniel Hartley</p>
      <p class="holder-title">Director</p>
    </div>

    <ul class="contact-list">
      <li>
        <svg class="contact-icon" viewBox="0 0 12 12" aria-hidden="true"><rect x="0.5" y="0.5" width="11" height="11" rx="1.5" fill="none" stroke="var(--brand-gold)"/><path d="M4 3h1.5l.6 1.6-.9.7a4 4 0 0 0 1.9 1.9l.7-.9L9.4 7.8V9.3A6 6 0 0 1 4 3z" fill="var(--brand-gold)"/></svg>
        <span>11 555 0192</span>
      </li>
      <li>
        <svg class="contact-icon" viewBox="0 0 12 12" aria-hidden="true"><rect x="0.5" y="0.5" width="11" height="11" rx="1.5" fill="var(--brand-gold)"/><path d="M2.5 4l3.5 2.5L9.5 4M2.5 4v4.5h7V4" fill="none" stroke="var(--ink-light)" stroke-width="0.9"/></svg>
        <span>hello@meadowestate.com</span>
      </li>
      <li>
        <svg class="contact-icon" viewBox="0 0 12 12" aria-hidden="true"><rect x="0.5" y="0.5" width="11" height="11" rx="1.5" fill="var(--brand-gold)"/><path d="M6 2.2a2.6 2.6 0 0 1 2.6 2.6C8.6 6.8 6 9.8 6 9.8S3.4 6.8 3.4 4.8A2.6 2.6 0 0 1 6 2.2z" fill="var(--ink-light)"/><circle cx="6" cy="4.8" r="0.9" fill="var(--brand-gold)"/></svg>
        <span>PO Box 4127</span>
      </li>
      <li class="contact-indent">Greenvale VIC 3059</li>
    </ul>
  </div>
</body>
</html>
```